Design eBook Cover for Homeowner Association (HOA) book

We need a cover design for an eBook entitled "The Residents Council Leader's Manual: Practical Steps and Proven Methods".

Title: The Residents Council Leader's Manual

Subtitle: Practical Steps and Proven Methods

Name of Author: Gerald Whitcombe, CMA

Style: Professional Guide

Testimonial: "This book is an indispensable tool for anyone on an HOA board. The expert advice and practical approach in 'The Residents Council Leader's Manual' have made a world of difference in our community. Every board member should have a copy!"
— Marla Quint, HOA Board President

I have uploaded a file as design inspiration but not locked into the colors or look. Just want a clean, professional looking cover.

Target Market(s)

Board members of HOAs (Homeowners associations) in the United States

Industry/Entity Type

Real Estate, HOA

Requirements
Must have
• Clean, professional appearance that conveys authority

```html
<!DOCTYPE html>
<html lang="en">
<head>
<meta charset="utf-8">
<title>The Residents Council Leader's Manual — Cover</title>
<link rel="stylesheet" href="https://fonts.googleapis.com/css2?family=Montserrat:wght@400;700;800;900&display=swap">
<style>
  :root {
    --stage: #000000;
    --cover-yellow: #ffcd00;
    --ink: #1f1f1d;
    --art-tone-a: #f7c400;
    --art-tone-b: #efbd00;
  }
  html, body {
    margin: 0;
    padding: 0;
    width: 1200px;
    height: 1159px;
    overflow: hidden;
    background: var(--stage);
  }
  .canvas {
    position: relative;
    width: 1200px;
    height: 1159px;
    background: var(--stage);
  }
  .book-cover {
    position: absolute;
    left: 247px;
    top: 50px;
    width: 706px;
    height: 1059px;
    background: var(--cover-yellow);
  }
  .title-block {
    position: absolute;
    left: 0;
    top: 0;
    width: 706px;
    height: 500px;
    font-family: "Montserrat", Arial, sans-serif;
    fill: var(--ink);
  }
  .title-block .rule { stroke: var(--ink); stroke-width: 4; }
  .title-the { font-weight: 700; font-size: 72px; }
  .title-main { font-weight: 900; font-size: 122px; }
  .title-mid { font-weight: 700; font-size: 56px; }
  .title-last { font-weight: 900; font-size: 104px; }
  .meeting-art {
    position: absolute;
    left: 61px;
    top: 541px;
    width: 592px;
    height: 244px;
    background: linear-gradient(180deg, var(--art-tone-a), var(--art-tone-b));
    border-radius: 6px;
  }
  .subtitle {
    position: absolute;
    left: 0;
    top: 790px;
    width: 706px;
    margin: 0;
    text-align: center;
    font-family: "Montserrat", Arial, sans-serif;
    font-weight: 400;
    font-size: 29px;
    line-height: 42px;
    letter-spacing: 1px;
    color: var(--ink);
    text-transform: uppercase;
  }
  .author {
    position: absolute;
    left: 0;
    top: 976px;
    width: 706px;
    margin: 0;
    text-align: center;
    font-family: "Montserrat", Arial, sans-serif;
    font-weight: 700;
    font-size: 33px;
    letter-spacing: 0.5px;
    color: #000;
    text-transform: uppercase;
  }
</style>
</head>
<body>
<main class="canvas">
  <section class="book-cover">
    <svg class="title-block" viewBox="0 0 706 500" role="heading" aria-level="1" aria-label="The Residents Council Leader's Manual">
      <line class="rule" x1="81" y1="132" x2="290" y2="132"/>
      <line class="rule" x1="448" y1="132" x2="634" y2="132"/>
      <text class="title-the" x="369" y="134" text-anchor="middle">THE</text>
      <text class="title-main" x="80" y="232" textLength="554" lengthAdjust="spacingAndGlyphs">RESIDENTS</text>
      <text class="title-main" x="80" y="339" textLength="554" lengthAdjust="spacingAndGlyphs">COUNCIL</text>
      <text class="title-mid" x="80" y="397" textLength="554" lengthAdjust="spacingAndGlyphs">LEADER’S</text>
      <text class="title-last" x="80" y="480" textLength="560" lengthAdjust="spacingAndGlyphs">MANUAL</text>
    </svg>

    <div class="meeting-art" role="img" aria-label="Single-line drawing of a board meeting: five people seated around a table while one person stands and speaks"></div>

    <p class="subtitle">Practical Steps<br>and Proven Methods</p>

    <p class="author">Gerald Whitcombe, CMA</p>
  </section>
</main>
</body>
</html>
```